Telmoro Business Card

I already have the conplay logo. I need to develop a professional business card layout

Target Market(s)

Business

Industry/Entity Type

Business

Contact Information for Business Card

Company Name: Telmoro Limited

Font styles to use
Sans Serif

Colors

Designer to choose colors to be used in the design.

Requirements
Must have
• Use current logo
• Need two card size options:
• Small Card: 70mm x 28mm (Landscape)
• Square Card: 65mm x 65mm
Nice to have
• I will need 8-10 files for each name, number and email address (details to follow)

```html
<!DOCTYPE html>
<html lang="en">
<head>
<meta charset="utf-8">
<title>Telmoro Limited – Business Card Options</title>
<link rel="stylesheet" href="https://fonts.googleapis.com/css2?family=Montserrat:wght@400;500;700&family=Oswald:wght@300;400&display=swap">
<style>
  :root{
    --page:#ffffff;
    --board:#3a3a3c;
    --card:#ffffff;
    --brand-navy:#2b3a8f;
    --sky:#29a8e0;
    --royal:#1f6fb5;
    --leaf:#8cc63f;
    --forest:#1e7d3c;
    --sun:#f7941d;
    --red:#ed1c24;
    --yellow:#f5e11a;
    --ink:#1a1a1a;
    --label:#ffffff;
  }
  *{box-sizing:border-box;margin:0;padding:0}
  html,body{width:1200px;height:1200px;overflow:hidden;background:var(--page)}
  body{font-family:"Montserrat",Arial,sans-serif;position:relative}
  .board{position:absolute;left:32px;top:32px;width:1136px;height:1136px;background:var(--board)}
  .option-label{position:absolute;color:var(--label);font-family:"Montserrat",Arial,sans-serif;font-weight:400;font-size:48px;line-height:1}
  .card{position:absolute;background:var(--card);overflow:hidden}
  .card--square-a{left:130px;top:86px;width:453px;height:453px}
  .card--square-b{left:130px;top:656px;width:453px;height:453px}
  .card--tall{left:762px;top:164px;width:305px;height:761px}

  .wordmark{position:absolute;display:flex;flex-direction:column;align-items:center;color:var(--brand-navy)}
  .wordmark__name{font-weight:700;line-height:1;letter-spacing:1px}
  .wordmark__tag{font-weight:500;letter-spacing:6px;margin-top:10px;font-size:15px;line-height:1}

  .person{position:absolute}
  .person__name{font-weight:700;font-size:24px;line-height:1}
  .person__role{font-size:13px;margin-top:8px;line-height:1}

  .contacts{position:absolute;list-style:none}
  .contact{display:flex;align-items:center;font-size:16.5px;line-height:1;height:18px}
  .contact svg{width:17px;height:17px;margin-right:7px;flex:none}

  .stripe{position:absolute;left:0;right:0}

  /* option 1 */
  .card--square-a .wordmark{left:29px;top:44px;width:255px}
  .card--square-a .wordmark__name{font-size:44px}
  .card--square-a .person{left:29px;top:156px}
  .card--square-a .person__name{color:var(--sky)}
  .card--square-a .person__role{color:var(--forest)}
  .card--square-a .contacts{left:29px;top:217px}
  .card--square-a .contact{position:absolute;white-space:nowrap}

  /* option 2 */
  .card--square-b .wordmark{left:98px;top:44px;width:255px}
  .card--square-b .wordmark__name{font-size:44px}
  .rule-set{position:absolute;top:44px;width:89px}
  .rule-set--left{left:0}
  .rule-set--right{right:0}
  .rule-set i{display:block;height:2px;margin-bottom:7px}
  .card--square-b .person{left:0;right:0;top:160px;text-align:center;color:var(--red)}
  .card--square-b .contacts{left:43px;top:305px;color:var(--ink)}
  .card--square-b .contact{position:absolute;white-space:nowrap}

  /* option 3 */
  .card--tall .wordmark{left:0;right:0;top:58px}
  .card--tall .wordmark__name{font-size:38px}
  .card--tall .wordmark__tag{font-size:14px}
  .name-band{position:absolute;left:0;right:0;top:240px;height:65px;background:var(--sky);color:#fff;text-align:center;padding-top:11px}
  .name-band .person__name{font-size:21px}
  .name-band .person__role{font-size:11px;margin-top:7px}
  .tall-detail{position:absolute;left:0;right:0;text-align:center;font-family:"Oswald",Arial,sans-serif;font-weight:300;font-size:21px;line-height:31px;color:var(--ink)}
  .tall-icon{position:absolute;left:140px;width:25px;height:25px}
</style>
</head>
<body>
<svg width="0" height="0" style="position:absolute" aria-hidden="true">
  <defs>
    <symbol id="i-pin" viewBox="0 0 20 20"><path d="M10 4.2a4 4 0 0 0-4 4c0 3 4 7.6 4 7.6s4-4.6 4-7.6a4 4 0 0 0-4-4zm0 5.6a1.6 1.6 0 1 1 0-3.2 1.6 1.6 0 0 1 0 3.2z"/></symbol>
    <symbol id="i-phone" viewBox="0 0 20 20"><path d="M7 4.5l2 2.6-1.2 1.4c.8 1.6 2 2.8 3.6 3.6l1.4-1.2 2.6 2-1.3 2.2c-4.8-.4-8.9-4.5-9.3-9.3z"/></symbol>
    <symbol id="i-globe" viewBox="0 0 20 20"><path fill="none" stroke="currentColor" stroke-width="1.2" d="M10 4.5a5.5 5.5 0 1 0 0 11 5.5 5.5 0 1 0 0-11zM4.5 10h11M10 4.5c-2.4 3-2.4 8 0 11M10 4.5c2.4 3 2.4 8 0 11M5.4 7.2h9.2M5.4 12.8h9.2"/></symbol>
    <symbol id="i-mail" viewBox="0 0 20 20"><path d="M5 6.5h10v7H5z"/><path fill="none" stroke-width="1.1" stroke="var(--env,#fff)" d="M5 6.7l5 4 5-4"/></symbol>
  </defs>
</svg>

<div class="board">
</div>
<span class="option-label" style="left:46px;top:48px">1.</span>
<span class="option-label" style="left:46px;top:600px">2.</span>
<span class="option-label" style="left:694px;top:48px">3.</span>

<!-- Option 1 -->
<section class="card card--square-a">
  <div class="wordmark"><span class="wordmark__name">TELMORO</span><span class="wordmark__tag">LIMITED</span></div>
  <div class="person"><p class="person__name">Dalen R. Whitcombe</p><p class="person__role">General Manager</p></div>
  <ul class="contacts">
    <li class="contact" style="top:62px;color:var(--leaf)"><svg viewBox="0 0 20 20"><circle cx="10" cy="10" r="10" fill="var(--leaf)"/><use href="#i-pin" fill="#fff"/></svg>1740 Harlowe Lane Brisbey, LA 70215</li>
    <li class="contact" style="top:92px;color:var(--sky)"><svg viewBox="0 0 20 20"><circle cx="10" cy="10" r="10" fill="var(--sky)"/><use href="#i-phone" fill="#fff"/></svg>555-014-2863</li>
    <li class="contact" style="top:121px;color:var(--sun)"><svg viewBox="0 0 20 20"><circle cx="10" cy="10" r="10" fill="var(--sun)"/><use href="#i-globe" color="#fff"/></svg>brightlineadvisory.com</li>
    <li class="contact" style="top:149px;color:var(--red)"><svg viewBox="0 0 20 20"><circle cx="10" cy="10" r="10" fill="var(--red)"/><use href="#i-mail" fill="#fff" style="--env:var(--red)"/></svg>dalen@brightlineadvisory.com</li>
  </ul>
  <div class="stripe" style="top:397px;height:7px;background:var(--royal)"></div>
  <div class="stripe" style="top:414px;height:7px;background:var(--yellow)"></div>
</section>

<!-- Option 2 -->
<section class="card card--square-b">
  <div class="rule-set rule-set--left"><i style="background:var(--forest)"></i><i style="background:var(--yellow)"></i><i style="background:var(--sky)"></i><i style="background:var(--sun)"></i><i style="background:var(--red)"></i></div>
  <div class="rule-set rule-set--right"><i style="background:var(--brand-navy)"></i><i style="background:var(--royal)"></i><i style="background:var(--brand-navy)"></i><i style="background:var(--sky)"></i><i style="background:var(--sun)"></i></div>
  <div class="wordmark"><span class="wordmark__name">TELMORO</span><span class="wordmark__tag">LIMITED</span></div>
  <div class="person"><p class="person__name">Dalen R. Whitcombe</p><p class="person__role">General Manager</p></div>
  <ul class="contacts">
    <li class="contact" style="top:0"><svg viewBox="0 0 20 20"><circle cx="10" cy="10" r="10" fill="var(--leaf)"/><use href="#i-pin" fill="#fff"/></svg>1740 Harlowe Lane Brisbey, LA 70215</li>
    <li class="contact" style="top:30px"><svg viewBox="0 0 20 20"><circle cx="10" cy="10" r="10" fill="var(--sky)"/><use href="#i-phone" fill="#fff"/></svg>555-014-2863</li>
    <li class="contact" style="top:58px"><svg viewBox="0 0 20 20"><circle cx="10" cy="10" r="10" fill="var(--sun)"/><use href="#i-globe" color="#fff"/></svg>brightlineadvisory.com</li>
    <li class="contact" style="top:88px"><svg viewBox="0 0 20 20"><circle cx="10" cy="10" r="10" fill="var(--red)"/><use href="#i-mail" fill="#fff" style="--env:var(--red)"/></svg>dalen@brightlineadvisory.com</li>
  </ul>
</section>

<!-- Option 3 -->
<section class="card card--tall">
  <div class="wordmark"><span class="wordmark__name">TELMORO</span><span class="wordmark__tag">LIMITED</span></div>
  <div class="stripe" style="top:226px;height:5px;background:var(--yellow)"></div>
  <div class="name-band person"><p class="person__name">Dalen R. Whitcombe</p><p class="person__role">General Manager</p></div>
  <div class="stripe" style="top:313px;height:5px;background:var(--yellow)"></div>

  <svg class="tall-icon" style="top:406px" viewBox="0 0 20 20"><circle cx="10" cy="10" r="10" fill="#111"/><use href="#i-pin" fill="var(--yellow)"/></svg>
  <p class="tall-detail" style="top:436px">1740 Harlowe Lane Brisbey<br>LA 70215</p>
  <svg class="tall-icon" style="top:510px" viewBox="0 0 20 20"><circle cx="10" cy="10" r="10" fill="#111"/><use href="#i-phone" fill="var(--leaf)"/></svg>
  <p class="tall-detail" style="top:541px">555-014-2863</p>
  <svg class="tall-icon" style="top:583px" viewBox="0 0 20 20"><circle cx="10" cy="10" r="10" fill="#111"/><use href="#i-globe" color="var(--sky)"/></svg>
  <p class="tall-detail" style="top:608px">brightlineadvisory.com</p>
  <svg class="tall-icon" style="top:649px" viewBox="0 0 20 20"><circle cx="10" cy="10" r="10" fill="#111"/><use href="#i-mail" fill="var(--red)" style="--env:#111"/></svg>
  <p class="tall-detail" style="top:680px">dalen@brightlineadvisory.com</p>
  <div class="stripe" style="top:730px;height:7px;background:var(--royal)"></div>
</section>
</body>
</html>
```